Business Card Design Project

I need a business card design for our new logo, please check the logo at the following link:
https://www.boxtrove.net/s/k7pqwe93mz41xr/TulipCrew.png
The address on the business card:
Av. Orlândio Vasconte 418 sala 207
Barra da Tijuca, Rio de Janeiro, RJ
CEP: 22719-480
Brasil
Phone: +55 21 74302186
e-mail: renato@tulipcrew.com.br
Updates
Thank you all for sending your designs, we will not provide feedback because there are too many designs, on December 3 we will pick the best design according to our point of view. Please keep posting.
Renato

```html
<!DOCTYPE html>
<html lang="pt-BR">
<head>
<meta charset="utf-8">
<title>TulipCrew – Cartão de visita</title>
<link rel="stylesheet" href="https://fonts.googleapis.com/css2?family=Delius&family=Yanone+Kaffeesatz:wght@500&display=swap">
<style>
  :root {
    --backdrop: #e4e4e2;
    --card-dark: #1b1d1e;
    --card-light: #ffffff;
    --gold: #e3b21a;
    --bronze: #5a4309;
    --ink: #1c1c1c;
    --brand-grey: #2c2f31;
    --text-soft: #b4b7b9;
  }
  html, body {
    margin: 0;
    width: 1200px;
    height: 900px;
    overflow: hidden;
    background: var(--backdrop);
  }
  .card {
    position: absolute;
    left: 110px;
    top: 170px;
    width: 980px;
    height: 560px;
    box-shadow: 0 14px 40px rgba(0,0,0,.35);
    overflow: hidden;
  }
  .card-art { position: absolute; inset: 0; }
  .brand-name {
    position: absolute;
    left: 150px;
    top: 150px;
    margin: 0;
    font-family: "Yanone Kaffeesatz", sans-serif;
    font-weight: 500;
    font-size: 92px;
    line-height: 1;
    color: var(--brand-grey);
    display: flex;
    align-items: center;
    gap: 16px;
  }
  .brand-mark {
    width: 34px;
    height: 34px;
    background: var(--gold);
  }
  .brand-vertical {
    position: absolute;
    left: 18px;
    bottom: 44px;
    margin: 0;
    font-family: "Yanone Kaffeesatz", sans-serif;
    font-weight: 500;
    font-size: 40px;
    letter-spacing: 2px;
    color: var(--gold);
    writing-mode: vertical-rl;
    transform: rotate(180deg);
  }
  .address {
    position: absolute;
    left: 82px;
    bottom: 44px;
    margin: 0;
    font-family: "Delius", sans-serif;
    font-style: normal;
    font-size: 17px;
    line-height: 1.5;
    color: var(--text-soft);
  }
  .contact {
    position: absolute;
    right: 42px;
    bottom: 52px;
    margin: 0;
    padding: 0;
    list-style: none;
    font-family: "Delius", sans-serif;
    font-size: 24px;
    color: var(--ink);
    text-align: right;
  }
  .contact li {
    display: flex;
    justify-content: flex-end;
    align-items: center;
    gap: 10px;
    margin-top: 12px;
  }
  .contact svg { width: 22px; height: 22px; }
</style>
</head>
<body>
  <div class="card">
    <svg class="card-art" viewBox="0 0 980 560" aria-hidden="true">
      <rect width="980" height="560" fill="var(--card-light)"/>
      <path d="M935,95 C945,270 730,470 400,560" fill="none" stroke="var(--bronze)" stroke-width="7"/>
      <path d="M0,0 H910 C985,170 700,470 300,560 H0 Z" fill="var(--card-dark)"/>
    </svg>

    <p class="brand-name"><span class="brand-mark"></span>TulipCrew</p>
    <p class="brand-vertical">TULIPCREW</p>

    <address class="address">
      Av. Orlândio Vasconte 418 sala 207<br>
      Barra da Tijuca, Rio de Janeiro, RJ<br>
      CEP: 22719-480<br>
      Brasil
    </address>

    <ul class="contact">
      <li>
        <svg viewBox="0 0 24 24" aria-hidden="true"><path d="M6.6 10.8a15 15 0 0 0 6.6 6.6l2.2-2.2a1 1 0 0 1 1-.25 11.4 11.4 0 0 0 3.6.6 1 1 0 0 1 1 1V20a1 1 0 0 1-1 1A17 17 0 0 1 3 4a1 1 0 0 1 1-1h3.5a1 1 0 0 1 1 1c0 1.25.2 2.45.6 3.6a1 1 0 0 1-.25 1z" fill="var(--ink)"/></svg>
        <span>+55 21 74302186</span>
      </li>
      <li>
        <svg viewBox="0 0 24 24" aria-hidden="true"><rect x="2.5" y="5" width="19" height="14" fill="none" stroke="var(--ink)" stroke-width="1.8"/><path d="M2.5 5l9.5 8 9.5-8" fill="none" stroke="var(--ink)" stroke-width="1.8"/></svg>
        <span>renato@tulipcrew.com.br</span>
      </li>
    </ul>
  </div>
</body>
</html>
```